Simple Business Cards for Self-employed Coach

Simple business card with a design that includes the QLT logo.
Using either only the logo color or additional colors that match the logo.

Meridian Guides reach deeply into the past, gathering wisdom from East and West, while still staying current with the frontiers of new discovery in cognitive science, genetics, and other disciplines. see https://www.brightharborpath.example/what-is-integral-coaching/

Target Market(s)

Coaching Clients in Tokyo /Asia; in business organizations, but also outside

Industry/Entity Type

Life Coaching

Contact Information for Business Card

Lukas Brenning
Certified Meridian Guide

3-2-48 Kamiyoshi
Nakarino 164-0392
Tokyo, Japan

Phone: +81 70 4817 5062
E-Mail: lukas.brenning@mailora.example

Font styles to use
Sans Serif

Colors
00a990

Requirements
Must have
• include uploaded logo
• color fitting with QLT logo color
Nice to have
• simple, elegant design
Should not have
• clutter

```html
<!DOCTYPE html>
<html lang="en">
<head>
<meta charset="utf-8">
<title>Lukas Brenning – Business Card</title>
<link rel="stylesheet" href="https://fonts.googleapis.com/css2?family=Open+Sans:wght@400;700&display=swap">
<style>
  :root {
    --teal: #447872;
    --white: #ffffff;
    --page: #ffffff;
  }
  * { margin: 0; padding: 0; box-sizing: border-box; }
  html, body {
    width: 1200px; height: 1200px; overflow: hidden;
    background: var(--page);
    font-family: "Open Sans", sans-serif;
  }
  .card {
    position: absolute; left: 173px; top: 329px;
    width: 845px; height: 475px;
    background: var(--white);
  }
  .panel { position: absolute; background: var(--teal); overflow: hidden; }
  .panel--name    { left: 438px; top: 0;     width: 407px; height: 194px; }
  .panel--address { left: 0;     top: 222px; width: 410px; height: 253px; }
  .panel--contact { left: 438px; top: 222px; width: 407px; height: 253px; }

  .brand {
    position: absolute; left: 41px; top: 40px;
    display: flex; align-items: center; gap: 18px;
    color: var(--teal); font-weight: 700; font-size: 76px; line-height: 1;
    letter-spacing: 0.06em;
  }
  .brand__square { width: 58px; height: 58px; background: var(--teal); }

  .person {
    position: absolute; right: 34px; top: 50px;
    text-align: center; color: var(--white);
  }
  .person__name  { font-weight: 700; font-size: 41px; line-height: 1.1; letter-spacing: -0.01em; white-space: nowrap; }
  .person__title { font-weight: 400; font-size: 22px; line-height: 1.4; white-space: nowrap; }

  .address {
    position: absolute; left: 41px; top: 83px;
    color: var(--white); font-weight: 700; font-size: 24px; line-height: 32px;
    font-style: normal; white-space: nowrap;
  }

  .contact-line {
    position: absolute; left: 25px;
    display: flex; align-items: center;
    color: var(--white); font-weight: 700; font-size: 17px;
    letter-spacing: -0.01em; white-space: nowrap;
  }
  .contact-line--phone { top: 68px; }
  .contact-line--email { top: 135px; }
  .contact-line svg { display: block; }
  .contact-line .icon-slot { width: 36px; display: flex; justify-content: center; margin-right: 15px; }
</style>
</head>
<body>
  <div class="card">
    <div class="brand">
      <span class="brand__square"></span>
      <span class="brand__name">QLT</span>
    </div>

    <div class="panel panel--name">
      <div class="person">
        <div class="person__name">Lukas Brenning</div>
        <div class="person__title">Certified Meridian Guide</div>
      </div>
    </div>

    <div class="panel panel--address">
      <address class="address">
        3-2-48 Kamiyoshi<br>
        Nakarino 164-0392<br>
        Tokyo, Japan
      </address>
    </div>

    <div class="panel panel--contact">
      <div class="contact-line contact-line--phone">
        <span class="icon-slot">
          <svg width="26" height="44" viewBox="0 0 26 44" aria-hidden="true">
            <rect x="2" y="2" width="22" height="40" rx="3" fill="none" stroke="#fff" stroke-width="2.5"/>
            <line x1="9" y1="6" x2="17" y2="6" stroke="#fff" stroke-width="1.5"/>
            <circle cx="13" cy="37" r="1.8" fill="#fff"/>
          </svg>
        </span>
        <span>+81 70 4817 5062</span>
      </div>
      <div class="contact-line contact-line--email">
        <span class="icon-slot">
          <svg width="36" height="28" viewBox="0 0 36 28" aria-hidden="true">
            <path d="M0 0 H36 V28 H0 Z" fill="#fff"/>
            <path d="M0 0 L18 15 L36 0" fill="none" stroke="#447872" stroke-width="2.5"/>
            <path d="M0 28 L13 13 M36 28 L23 13" stroke="#447872" stroke-width="2.5"/>
          </svg>
        </span>
        <span>lukas.brenning@mailora.example</span>
      </div>
    </div>
  </div>
</body>
</html>
```